A new website for Electrical Contractor Business

We are looking for a unique and new WordPress website design which would include 5 Pages - Home Page, Meet the Team, Our Services, Our Projects and Contact Us page.

The global theme for the website needs to be professional but simple to navigate as we cater for both business and home owner customers.

Our core business service is targeted around lighting from single room decorative to large office so the theme should incorporate this in some way.

The home page should include;
Our business logo, Contact number, Email address, small Image rotation box - Highlighting pervious projectsText box - With welcome message, chirpnet feed news reel/Customer feed back box.

I would also like to see a 2 boxes for the separate customer types we services. Business and Home Owner. each box will have a small image with a small text description with a link to the area of the services page relevant to that customer type.

Meet the team page -This will be introducing potential customers to the team so I would like it to include for each team member. Something like a small image and text area which will introduce an outline of the team members skills and abilities.

Our Services page This page will be outlining the different services on offer to the both customer types business and homeowner. Each service should have an image with text description of the service would good here.

Our projects page-Will include images of pervious projects and work we have completed along with a text area for the project description/ outliner.

Contact Us page - Should include a contact form which should include an option for the customer to quest us to call them back, also a selection box for them to inform us our how they found our details would be good.

Colour - The theme colours can be taken from the logo or feel free to impress with your own imagination.

Remember we are looking for a website that will interest our customers enough to except our services or be drawn further into the website.. So call to action links to other areas of the site/ contact page are welcome

Target Market(s)

Business - Office, warehousing and Large Store - lighting and Power
Home owner lighting and power

Coding

Coded - Design and coding required

Number of Pages Required

5+ page

Font styles to use
Serif
Sans Serif

Colors

Designer to choose colors to be used in the design.

Requirements
Must have
• Logo integrated into the website design - i.e. website colours which allow the logo to blend into the design.
Nice to have
• Custom but professional theme catering to business customers, but also show that we do provide services to home owners too.
Should not have
• Sorry am not interested in one oversized block image on rotation covering half the home page.. Images will be needed but not a single block over sized frame with not text, shape. Please use your imagination when considering this design

```html
<!DOCTYPE html>
<html lang="en">
<head>
<meta charset="utf-8">
<title>Brightline Electrical – Lighting for Business and Home</title>
<link href="https://fonts.googleapis.com/css2?family=Open+Sans:wght@400;600;700&family=Merriweather:wght@400;700&family=Lato:wght@400;700&display=swap" rel="stylesheet">
<style>
:root{
  --navy:#1d2f5e;
  --navy-deep:#15234a;
  --navy-dark:#0f1a36;
  --orange:#f26b21;
  --orange-soft:#f58a3c;
  --ink:#333a45;
  --muted:#6b7380;
  --line:#d9dde4;
  --paper:#ffffff;
  --mist:#f2f3f5;
  --sky:#e3ebf6;
}
*{box-sizing:border-box;margin:0;padding:0}
html,body{width:1200px;height:3920px;overflow:hidden}
body{font-family:"Open Sans",Arial,sans-serif;color:var(--ink);background:var(--paper);position:relative}
.btn{display:inline-block;font-family:"Open Sans",Arial,sans-serif;font-size:14px;font-weight:600;color:#fff;background:var(--navy);padding:10px 20px;border-radius:2px;text-decoration:none}
.btn--orange{background:var(--orange)}
.section-title{font-family:"Merriweather",Georgia,serif;font-size:38px;font-weight:400;text-align:center;color:var(--navy)}
.section-title span{color:var(--orange)}
.img-fill{display:block}

/* top bar */
.topbar{height:40px;background:var(--navy-dark);display:flex;justify-content:flex-end;align-items:center;padding:0 60px;gap:16px;font-size:12px;color:#cfd5e2}
.topbar .sep{opacity:.5}
.topbar .dots{display:flex;gap:8px}
.topbar .dots i{width:12px;height:12px;border-radius:50%;background:#8d97ad;display:block}

/* header */
.header{height:80px;display:flex;align-items:center;padding:0 170px;gap:120px}
.brand{display:flex;align-items:center;gap:12px}
.brand-mark{width:40px;height:40px;border-radius:50%;background:var(--orange)}
.brand-name{font-family:"Open Sans",Arial,sans-serif;font-weight:700;font-size:24px;letter-spacing:1px;color:var(--navy)}
.search{width:560px;height:40px;border:1px solid var(--line);border-radius:20px;display:flex;align-items:center;padding:0 18px;font-size:13px;color:#9aa1ad;justify-content:space-between}

/* nav */
.nav{height:60px;background:var(--mist);display:flex;align-items:center;padding:0 170px;justify-content:space-between}
.nav ul{display:flex;list-style:none;height:60px}
.nav li{display:flex;align-items:center;padding:0 22px;font-size:13px;font-weight:600;color:var(--navy)}
.nav li.active{background:var(--navy);color:#fff}
.call{display:flex;align-items:center;gap:8px;background:var(--orange);color:#fff;font-size:13px;font-weight:700;padding:10px 18px;border-radius:20px}

/* hero */
.hero{position:relative;height:480px}
.hero .img-fill{position:absolute;inset:0;background:linear-gradient(120deg,#6f6458 0%,#c9b9a4 35%,#8e7f6e 60%,#3e3a38 100%)}
.hero-copy{position:absolute;left:0;right:0;top:230px;text-align:center}
.hero-copy h1{display:inline-block;font-family:"Lato",Arial,sans-serif;font-weight:700;font-size:50px;color:#fff;background:rgba(242,107,33,.88);padding:4px 18px}
.hero-copy .btn{margin-top:18px}
.hero-arrow{position:absolute;top:220px;width:28px;height:44px;background:rgba(15,26,54,.75);display:flex;align-items:center;justify-content:center}
.hero-arrow--left{left:0}.hero-arrow--right{right:0}

/* services */
.services{height:480px;padding-top:68px}
.service-row{display:flex;gap:40px;margin:50px 0 0 28px}
.service{display:flex;gap:28px;width:560px}
.service .img-fill{width:264px;height:220px;flex:none}
.service h3{font-size:16px;font-weight:700;color:var(--ink);margin-top:24px;text-transform:uppercase}
.service p{font-size:13px;line-height:1.6;color:var(--muted);margin:8px 0 16px}

/* projects */
.projects{height:760px;background:linear-gradient(135deg,var(--navy-deep),var(--navy) 50%,var(--navy-deep));padding-top:56px;position:relative;overflow:hidden}
.projects .section-title{color:#fff}
.projects-bg{position:absolute;inset:0}
.project-grid{position:relative;display:grid;grid-template-columns:repeat(4,267px);grid-template-rows:200px 216px;gap:24px 24px;margin:46px 0 0 28px}
.project-grid .tall{grid-column:4;grid-row:1/3}
.projects .cta{position:relative;text-align:center;margin-top:56px}

/* feedback */
.feedback{height:520px;background:linear-gradient(180deg,#f4f7fb,var(--sky));padding-top:64px;position:relative}
.quote-card{display:flex;width:1008px;height:300px;margin:40px auto 0;background:#fff;box-shadow:0 6px 18px rgba(29,47,94,.15)}
.quote-card .img-fill{width:300px;height:300px;background:linear-gradient(160deg,#cfd8e4,#6e7f98)}
.quote-body{flex:1;text-align:center;padding:70px 60px 0}
.quote-body blockquote{font-family:"Merriweather",Georgia,serif;font-size:19px;line-height:1.6;color:var(--ink)}
.quote-body .who{margin-top:40px;font-size:13px;color:var(--muted)}
.quote-body .role{font-size:13px;font-weight:600;color:var(--ink);margin-top:4px}
.side-arrow{position:absolute;top:230px}
.side-arrow--left{left:40px}.side-arrow--right{right:40px}
.dots{display:flex;justify-content:center;gap:8px;margin-top:22px}
.dots i{width:9px;height:9px;border-radius:50%;background:#b5bfce;display:block}
.dots i.on{background:var(--navy)}

/* team */
.team{height:440px;position:relative;padding-top:106px}
.team>.img-fill{position:absolute;inset:0;background:linear-gradient(180deg,#3a3532,#5a4a3c 55%,#2a2624)}
.team .section-title{position:relative;color:#fff}
.member{position:relative;display:flex;align-items:center;width:860px;height:172px;margin:38px 0 0 160px;background:rgba(29,47,94,.92);padding:0 16px;gap:24px}
.member .img-fill{width:144px;height:144px;background:linear-gradient(160deg,#d7dde6,#8a95a6);flex:none}
.member .bio{flex:1;color:#e1e6f0;font-size:13px;line-height:1.6}
.member .bio strong{display:block;color:#fff;margin-top:10px}
.member .social{display:flex;gap:14px;padding-right:30px;border-left:1px solid rgba(255,255,255,.3);padding-left:30px;height:100px;align-items:center}
.member .social i{width:16px;height:16px;background:#fff;border-radius:3px;display:block}
.pager{position:relative;display:flex;justify-content:center;gap:6px;margin-top:24px}
.pager span{width:26px;height:26px;background:#fff;display:flex;align-items:center;justify-content:center}

/* contact */
.contact{height:540px;background:var(--mist);padding-top:58px}
.contact .sub{text-align:center;font-size:14px;color:var(--muted);margin-top:10px}
.form{width:856px;margin:28px auto 0;display:grid;grid-template-columns:1fr 1fr;gap:12px 28px}
.field{height:36px;background:#fff;border:1px solid var(--line);font-size:13px;color:#8a919c;padding:9px 12px}
.field--msg{grid-column:1/3;height:96px}
.submit{grid-column:1/3;height:38px;background:var(--navy);color:#fff;font-size:13px;font-weight:700;display:flex;align-items:center;justify-content:center;margin-top:12px}

/* footer */
.footer{height:520px;position:relative;color:#cdd4e2}
.footer>.img-fill{position:absolute;inset:0;background:linear-gradient(180deg,#1a2647,#233560 60%,#1a2647)}
.footer-cols{position:relative;display:flex;padding:110px 0 0 170px;gap:90px}
.footer-about{width:240px;font-size:12px;line-height:1.7}
.footer-about .brand{margin-bottom:20px}
.footer-about .brand-name{color:#fff;font-size:20px}
.footer-about .more{color:var(--orange)}
.footer-contact{width:300px;font-size:12px;line-height:1.7}
.footer-contact h4{color:var(--orange);font-size:14px;margin-bottom:14px;text-transform:uppercase}
.footer-contact li{list-style:none;display:flex;gap:10px;margin-bottom:10px}
.feed{width:240px;height:250px;background:#fff;color:var(--ink);font-size:11px;margin-top:6px}
.feed-head{background:#4aa3df;color:#fff;font-weight:700;padding:6px 10px;font-size:12px}
.feed-item{display:flex;gap:8px;padding:10px;border-bottom:1px solid #eee;line-height:1.4}
.feed-item i{width:26px;height:26px;background:#c8d3e3;flex:none;display:block}
.copyright{position:absolute;left:0;right:0;bottom:24px;text-align:center;font-size:12px;color:#9aa4ba}
</style>
</head>
<body>

<div class="topbar">
  <span>Welcome to Brightline Electrical</span><span class="sep">|</span>
  <span>Language</span><span class="sep">|</span><span>English</span><span class="sep">|</span>
  <span>Login / Register</span>
  <span class="dots"><i></i><i></i><i></i><i></i><i></i></span>
</div>

<header class="header">
  <div class="brand"><span class="brand-mark"></span><span class="brand-name">BRIGHTLINE</span></div>
  <div class="search"><span>Search</span>
    <svg width="14" height="14" viewBox="0 0 14 14"><circle cx="6" cy="6" r="4.5" fill="none" stroke="#9aa1ad" stroke-width="1.6"/><line x1="9.5" y1="9.5" x2="13" y2="13" stroke="#9aa1ad" stroke-width="1.6"/></svg>
  </div>
</header>

<nav class="nav">
  <ul>
    <li class="active">HOME</li><li>OUR SERVICES</li><li>PROJECTS</li><li>MEET THE TEAM</li><li>CONTACT US</li>
  </ul>
  <div class="call">
    <svg width="14" height="14" viewBox="0 0 24 24"><path fill="#fff" d="M6.6 10.8a15.1 15.1 0 0 0 6.6 6.6l2.2-2.2a1 1 0 0 1 1-.25 11.4 11.4 0 0 0 3.6.57 1 1 0 0 1 1 1V20a1 1 0 0 1-1 1A17 17 0 0 1 3 4a1 1 0 0 1 1-1h3.5a1 1 0 0 1 1 1c0 1.25.2 2.45.57 3.57a1 1 0 0 1-.25 1z"/></svg>
    CALL US NOW
  </div>
</nav>

<section class="hero">
  <div class="img-fill" role="img" aria-label="Warmly lit living room with pendant lamps, fireplace and sofa"></div>
  <div class="hero-arrow hero-arrow--left"><svg width="10" height="16" viewBox="0 0 10 16"><path d="M8 2 2 8l6 6" fill="none" stroke="#fff" stroke-width="2"/></svg></div>
  <div class="hero-arrow hero-arrow--right"><svg width="10" height="16" viewBox="0 0 10 16"><path d="M2 2l6 6-6 6" fill="none" stroke="#fff" stroke-width="2"/></svg></div>
  <div class="hero-copy">
    <h1>Light Up Your World</h1><br>
    <a class="btn">View Projects</a>
  </div>
</section>

<section class="services">
  <h2 class="section-title"><span>Our</span> Services</h2>
  <div class="service-row">
    <article class="service">
      <div class="img-fill" role="img" aria-label="Bright open-plan office with ceiling lighting" style="background:linear-gradient(160deg,#e9eef2,#9aa6b3)"></div>
      <div>
        <h3>Lighting for Business</h3>
        <p>Offices, warehouses and large stores lit for comfort, safety and lower running costs.</p>
        <a class="btn">View Service Details</a>
      </div>
    </article>
    <article class="service">
      <div class="img-fill" role="img" aria-label="Modern living room with decorative lighting" style="background:linear-gradient(160deg,#f1ebe2,#b7a48f)"></div>
      <div>
        <h3>Lighting for Home</h3>
        <p>Decorative and practical lighting for every room, from one lamp to a full rewire.</p>
        <a class="btn">View Service Details</a>
      </div>
    </article>
  </div>
</section>

<section class="projects">
  <svg class="projects-bg" width="1200" height="760" aria-hidden="true">
    <polygon points="0,420 260,300 420,760 0,760" fill="#24386e" opacity=".5"/>
    <polygon points="820,0 1200,0 1200,380" fill="#24386e" opacity=".5"/>
    <polygon points="560,760 900,480 1200,760" fill="#162a58" opacity=".6"/>
  </svg>
  <h2 class="section-title"><span>Our</span> Projects</h2>
  <div class="project-grid">
    <div class="img-fill" role="img" aria-label="Yellow-lit lounge interior" style="background:linear-gradient(150deg,#e2c46e,#8a6b2f)"></div>
    <div class="img-fill" role="img" aria-label="Living room with recessed ceiling lights" style="background:linear-gradient(150deg,#9a8a78,#3c3128)"></div>
    <div class="img-fill" role="img" aria-label="White office with shelving and panel lights" style="background:linear-gradient(150deg,#f1f3f6,#a9b6c6)"></div>
    <div class="img-fill tall" role="img" aria-label="Office corridor with green wall and spotlights" style="background:linear-gradient(170deg,#4d6a8a,#b4c640 55%,#2c3a4e)"></div>
    <div class="img-fill" role="img" aria-label="Pink room with crystal chandelier" style="background:linear-gradient(150deg,#f2b8c6,#b45a74)"></div>
    <div class="img-fill" role="img" aria-label="Warm living room with ceiling lighting" style="background:linear-gradient(150deg,#c89a70,#4a3222)"></div>
    <div class="img-fill" role="img" aria-label="Timber interior with soft wall lighting" style="background:linear-gradient(150deg,#e3c7a2,#8c6a46)"></div>
  </div>
  <div class="cta"><a class="btn btn--orange">View All Our Projects</a></div>
</section>

<section class="feedback">
  <h2 class="section-title" style="color:var(--orange)">Customer <span style="color:var(--orange)">Feed Back</span></h2>
  <svg class="side-arrow side-arrow--left" width="34" height="20" viewBox="0 0 34 20"><path d="M33 10H3M11 2 3 10l8 8" fill="none" stroke="var(--orange)" stroke-width="2"/></svg>
  <svg class="side-arrow side-arrow--right" width="34" height="20" viewBox="0 0 34 20"><path d="M1 10h30M23 2l8 8-8 8" fill="none" stroke="var(--orange)" stroke-width="2"/></svg>
  <div class="quote-card">
    <div class="img-fill" role="img" aria-label="Portrait of a smiling client in a suit"></div>
    <div class="quote-body">
      <blockquote>Ut nec viverra magna. Cras vel sollicitudin ipsum. Pellentesque aliquam egestas orci.</blockquote>
      <p class="who">Daniel Marsh</p>
      <p class="role">Project Manager, Northgate Offices</p>
    </div>
  </div>
  <div class="dots"><i class="on"></i><i></i><i></i></div>
</section>

<section class="team">
  <div class="img-fill" role="img" aria-label="Dimly lit room filled with hanging filament bulbs"></div>
  <h2 class="section-title"><span>Our</span> Team</h2>
  <div class="member">
    <div class="img-fill" role="img" aria-label="Portrait of the company founder"></div>
    <div class="bio">
      Qualified electrician with twenty years in commercial and home lighting, leading every project from design to switch-on.
      <strong>Oliver Grant</strong>
      Founder, Senior Electrician
    </div>
    <div class="social"><i></i><i></i><i></i><i></i></div>
  </div>
  <div class="pager">
    <span><svg width="8" height="12" viewBox="0 0 8 12"><path d="M7 1 2 6l5 5" fill="none" stroke="var(--navy)" stroke-width="2"/></svg></span>
    <span><svg width="8" height="12" viewBox="0 0 8 12"><path d="M1 1l5 5-5 5" fill="none" stroke="var(--navy)" stroke-width="2"/></svg></span>
  </div>
</section>

<section class="contact">
  <h2 class="section-title"><span>Contact</span> Us Today!</h2>
  <p class="sub">Please contact us with any questions</p>
  <div class="form">
    <div class="field">Name</div>
    <div class="field">Phone No</div>
    <div class="field">Email Address</div>
    <div class="field">Address</div>
    <div class="field field--msg">Message</div>
    <div class="submit">SUBMIT</div>
  </div>
</section>

<footer class="footer">
  <div class="img-fill" role="img" aria-label="Dark blue background of glowing light bulbs"></div>
  <div class="footer-cols">
    <div class="footer-about">
      <div class="brand"><span class="brand-mark" style="width:32px;height:32px"></span><span class="brand-name">BRIGHTLINE</span></div>
      <p>Local electrical contractors lighting offices, stores and homes with care, safe work and honest pricing. <span class="more">More</span></p>
    </div>
    <div class="footer-contact">
      <h4>Contact</h4>
      <ul>
        <li><svg width="12" height="14" viewBox="0 0 12 14"><path d="M6 0a5 5 0 0 0-5 5c0 3.8 5 9 5 9s5-5.2 5-9a5 5 0 0 0-5-5zm0 7a2 2 0 1 1 0-4 2 2 0 0 1 0 4z" fill="var(--orange)"/></svg>48 Harbour Lane, Westfield</li>
        <li><svg width="14" height="10" viewBox="0 0 14 10"><rect x=".5" y=".5" width="13" height="9" fill="none" stroke="var(--orange)"/><path d="M.5.5 7 6 13.5.5" fill="none" stroke="var(--orange)"/></svg>hello@brightline-electrical.example</li>
        <li><svg width="12" height="12" viewBox="0 0 24 24"><path fill="var(--orange)" d="M6.6 10.8a15.1 15.1 0 0 0 6.6 6.6l2.2-2.2a1 1 0 0 1 1-.25 11.4 11.4 0 0 0 3.6.57 1 1 0 0 1 1 1V20a1 1 0 0 1-1 1A17 17 0 0 1 3 4a1 1 0 0 1 1-1h3.5a1 1 0 0 1 1 1c0 1.25.2 2.45.57 3.57a1 1 0 0 1-.25 1z"/></svg>01 555 0148</li>
      </ul>
    </div>
    <div class="feed">
      <div class="feed-head">chirpnet</div>
      <div class="feed-item"><i></i><span>New office fit-out finished this week, fully LED lit.</span></div>
      <div class="feed-item"><i></i><span>Book a free home lighting check this month.</span></div>
      <div class="feed-item"><i></i><span>Warehouse relamp cut energy use by forty percent.</span></div>
    </div>
  </div>
  <p class="copyright">© 2016 Brightline Electrical. All Rights Reserved.</p>
</footer>

</body>
</html>
```